I need a creative wine label design for my brand called ZAP ZEE. A design that catches the eye of the millennial consumer! Something very creative and playing off of the ZAP ZEE concept.

This will be a Red Blend 2019 vintage from California

Target Market(s)

Millennial wine consumer

Requirements
Must have
• Must have a design that attracts the millennial wine consumer. This must have creative flare.
Should not have
• Nothing corny!

```html
<!DOCTYPE html>
<html lang="en">
<head>
<meta charset="UTF-8">
<title>ZAP ZEE Red Blend 2019 Label</title>
<link rel="stylesheet" href="https://fonts.googleapis.com/css2?family=Questrial&family=Marcellus&display=swap">
<style>
  :root {
    --backdrop: #1f1a17;
    --label-cream: #f3f1c6;
    --label-glow: #ffffff;
    --rule-red: #c8302f;
    --brand-grey: #6b6b6b;
    --wine-red: #a6252a;
    --ornament-tone: #9a9890;
  }
  html, body {
    margin: 0;
    padding: 0;
    overflow: hidden;
    background: var(--backdrop);
  }
  .canvas {
    position: relative;
    width: 1200px;
    height: 1000px;
    background: var(--backdrop);
    overflow: hidden;
  }
  .label-shape {
    position: absolute;
    left: 0;
    top: 0;
    width: 1200px;
    height: 1000px;
  }
  .ornament {
    position: absolute;
    top: 367px;
    width: 95px;
    height: 107px;
    border-radius: 40%;
    background: radial-gradient(ellipse at center, var(--ornament-tone) 0%, rgba(154,152,144,0.35) 55%, rgba(154,152,144,0) 75%);
  }
  .ornament--left { left: 287px; }
  .ornament--right { left: 885px; }
  .brand-name {
    position: absolute;
    left: 380px;
    width: 490px;
    top: 368px;
    margin: 0;
    text-align: center;
    font-family: "Questrial", "Helvetica Neue", sans-serif;
    font-weight: 400;
    font-size: 96px;
    line-height: 96px;
    letter-spacing: 4px;
    color: var(--brand-grey);
  }
  .wine-type {
    position: absolute;
    left: 300px;
    width: 682px;
    top: 538px;
    margin: 0;
    text-align: center;
    font-family: "Marcellus", "Times New Roman", serif;
    font-weight: 400;
    font-size: 60px;
    line-height: 64px;
    letter-spacing: 2px;
    color: var(--wine-red);
  }
  .vintage-origin {
    position: absolute;
    left: 300px;
    width: 682px;
    top: 608px;
    margin: 0;
    text-align: center;
    font-family: "Marcellus", "Times New Roman", serif;
    font-weight: 400;
    font-size: 36px;
    line-height: 40px;
    letter-spacing: 2px;
    color: var(--wine-red);
  }
</style>
</head>
<body>
  <main class="canvas">
    <svg class="label-shape" viewBox="0 0 1200 1000" xmlns="http://www.w3.org/2000/svg" aria-hidden="true">
      <defs>
        <radialGradient id="label-glow" cx="0.5" cy="0.55" r="0.55">
          <stop offset="0" stop-color="var(--label-glow)" />
          <stop offset="1" stop-color="var(--label-cream)" />
        </radialGradient>
      </defs>
      <polygon class="label-hexagon" points="639,124 1023,307 1023,662 639,864 256,662 256,307" fill="url(#label-glow)" />
      <polygon class="label-rule" points="639,138 1010,314 1010,654 639,850 269,654 269,314" fill="none" stroke="var(--rule-red)" stroke-width="1.5" />
    </svg>

    <div class="ornament ornament--left" role="img" aria-label="Grey flourish ornament to the left of the brand name"></div>
    <h1 class="brand-name">ZAP ZEE</h1>
    <div class="ornament ornament--right" role="img" aria-label="Grey flourish ornament to the right of the brand name"></div>

    <p class="wine-type">RED BLEND 2019</p>
    <p class="vintage-origin">VINTAGE FROM CALIFORNIA</p>
  </main>
</body>
</html>
```